New concept travel "Fun" for young people !
----- Lingo Converter ----
With our skills, our agency was the first to develop spring break concepts in French-speaking Belgium by bringing together hundreds of students in Spain to celebrate!
Following a concern for health, our usual graphic designer can not take care of our achievements.
We are looking for a person in the long term (= serious work, contact exchanges and other "contracts").
We will also need a socialbook cover and a single-sided A4 poster.
The name of the concept is GOLDEN DRIFT.
You will be free to create a beautiful new logo of course.
This one could possibly be put on future t-shirts for our staff of animators during the trip or offered to the public!
Here is the job to do:
- Objective NEW CONCEPT 2018 in Bulgaria -
We need a visual (efficient and dynamic flyer to attract a population between 21 and 35 years old.
Flyer idea: A6 landscape postcard format, vintage, with a beautiful visual on the front that makes you want and arouse curiosity (with title of the trip "GOLDEN DRIFT - Bulgaria 2018") and the mention "New Concept" with our logo MORALIX TOURS .
On the back, on the left half of the postcard: a sweet little word from a woman, the style "Hey ! Le soleil est bien là, les cocktails sont savoureux et l'ambiance incroyable ! On t'attends avec les filles ! Je t'embrasse. Nora" with a fake kiss (= smack).
On the right half, useful information to stay to know:
- du samedi 1 au samedi 8 septembre 2018
- Plages Céleste, Bulgarie
- Voyage "tout compris" : vol aller-retour, hôtel 4**** formule ALL INCLUSIVE, entrées en boites, cocktails offerts, beach party, ... & bien plus !
- prix : € 599,00 par personne en chambre double
- plus d'infos sur www.golden-drift-trips.com ou au 0472 818 604
Here is the logo of our agency + some visuals of our last trip to Hungary (just to give you a little effect to feel ATTENTION I want something else here not copy please, please)
Good luck to everyone !

```html
<!DOCTYPE html>
<html lang="fr">
<head>
<meta charset="utf-8">
<title>Golden Drift – Bulgarie 2018 – Carte postale verso</title>
<link rel="stylesheet" href="https://fonts.googleapis.com/css2?family=Archivo+Narrow:wght@500;700&family=Silkscreen:wght@400;700&family=Cedarville+Cursive&display=swap">
<style>
  :root {
    --sky: #1e9ad6;
    --sky-pale: #bfe2f3;
    --sky-mist: #e9f6fc;
    --steel: #9fc2d3;
    --sand: #cdb7a0;
    --rust: #c0642a;
    --orange: #e07b36;
    --ink: #1c1c1c;
    --ink-soft: #2c3440;
    --white: #ffffff;
    --dots: #9a8c86;
    --lips: #d0506f;
  }
  * { margin: 0; padding: 0; box-sizing: border-box; }
  html, body { width: 1200px; height: 848px; overflow: hidden; background: #ffffff; }
  .postcard {
    position: relative;
    width: 1200px; height: 848px;
    overflow: hidden;
    background:
      linear-gradient(90deg,
        var(--sky-pale) 0%, var(--sky-mist) 25%, #ffffff 44%,
        #e3eef3 48%, var(--steel) 58%, #b9c2c2 70%, var(--sand) 82%, var(--orange) 100%);
  }
  .message-side {
    position: absolute; left: 0; top: 0; width: 600px; height: 848px;
    background: linear-gradient(160deg, var(--sky-pale) 0%, var(--sky-mist) 35%, rgba(255,255,255,0.9) 75%, #ffffff 100%);
  }

  /* brand */
  .brand {
    position: absolute; left: 0; top: 17px;
    width: 340px; height: 68px;
    background: var(--sky);
    display: flex; align-items: center; gap: 12px; padding-left: 18px;
  }
  .brand-dot { flex: none; width: 14px; height: 14px; background: var(--white); border-radius: 50%; }
  .brand-name {
    font-family: "Archivo Narrow", sans-serif; font-weight: 700;
    font-size: 38px; line-height: 1; color: var(--white); letter-spacing: 1px;
    white-space: nowrap;
  }
  .concept-tag {
    position: absolute; left: 44px; top: 104px;
    font-family: "Cedarville Cursive", cursive; font-weight: 700;
    font-size: 30px; color: var(--rust);
  }

  /* handwritten note */
  .note { position: absolute; left: 30px; top: 210px; width: 560px; }
  .note-line {
    position: relative; height: 64px;
    border-bottom: 2px dotted var(--dots);
  }
  .note-text {
    position: absolute; left: 6px; bottom: 2px;
    font-family: "Cedarville Cursive", cursive;
    font-size: 34px; color: var(--rust);
    transform: rotate(-5deg); transform-origin: left bottom;
    white-space: nowrap;
  }
  .signature {
    position: absolute; left: 150px; top: 616px;
    font-family: "Cedarville Cursive", cursive;
    font-size: 34px; color: var(--rust);
    transform: rotate(-5deg);
  }
  .kiss { position: absolute; left: 310px; top: 662px; width: 240px; height: 116px; }

  /* info side */
  .dates {
    position: absolute; left: 640px; top: 17px; width: 528px; height: 96px;
    background: var(--orange);
    text-align: center;
  }
  .dates-range {
    display: block; margin-top: 6px;
    font-family: "Archivo Narrow", sans-serif; font-weight: 500;
    font-size: 34px; line-height: 38px; color: var(--white);
  }
  .dates-month {
    position: absolute; left: 32px; top: 46px; width: 464px; height: 44px;
    background: var(--white);
    font-family: "Archivo Narrow", sans-serif; font-weight: 700;
    font-size: 42px; line-height: 44px; color: var(--orange);
  }
  .info { position: absolute; left: 620px; top: 170px; width: 560px; text-align: center; }
  .resort, .country {
    font-family: "Silkscreen", sans-serif; font-weight: 700; color: var(--ink);
  }
  .resort { font-size: 26px; line-height: 40px; letter-spacing: 1px; }
  .country { font-size: 46px; line-height: 60px; letter-spacing: 1px; }
  .feature-list { list-style: none; }
  .feature-list li, .highlight {
    font-family: "Archivo Narrow", sans-serif; font-weight: 700;
    font-size: 31px; line-height: 32px; color: var(--ink-soft);
  }
  .trip-basics { margin-top: 6px; }
  .highlight { color: var(--orange); }
  .formula { margin-top: 36px; }
  .extras { margin-top: 26px; }

  .price {
    position: absolute; left: 750px; top: 612px; width: 300px; height: 82px;
    background: var(--orange); border-radius: 41px;
    border: 3px solid var(--white);
    text-align: center; color: var(--white);
    font-family: "Archivo Narrow", sans-serif;
  }
  .price-amount { display: block; font-weight: 700; font-size: 34px; line-height: 36px; margin-top: 4px; }
  .price-terms { display: block; font-weight: 500; font-size: 13px; line-height: 14px; }

  .contact {
    position: absolute; left: 720px; top: 716px; width: 430px; height: 104px;
    background: var(--sky);
    transform: skewX(-8deg) rotate(-2deg);
    box-shadow: 0 3px 6px rgba(0,0,0,0.15);
  }
  .contact-text {
    transform: skewX(8deg);
    padding-top: 12px; text-align: center; color: var(--white);
    font-family: "Archivo Narrow", sans-serif; font-weight: 700;
    font-size: 21px; line-height: 26px;
  }
</style>
</head>
<body>
<main class="postcard">
  <section class="message-side">
    <div class="brand">
      <span class="brand-dot"></span>
      <span class="brand-name">MORALIX TOURS</span>
    </div>
    <p class="concept-tag">Nouveau Concept</p>

    <div class="note">
      <div class="note-line"><span class="note-text">Hey ! Le soleil est bien là,</span></div>
      <div class="note-line"><span class="note-text">les cocktails sont savoureux</span></div>
      <div class="note-line"><span class="note-text">et l'ambiance incroyable !</span></div>
      <div class="note-line"><span class="note-text">On t'attends avec les filles !</span></div>
      <div class="note-line"><span class="note-text">Je t'embrasse...</span></div>
    </div>
    <p class="signature">Nora.</p>

    <svg class="kiss" viewBox="0 0 240 116" role="img" aria-label="Empreinte de baiser rose au rouge à lèvres">
      <ellipse cx="120" cy="58" rx="116" ry="50" fill="var(--lips)" opacity="0.85"/>
    </svg>
  </section>

  <header class="dates">
    <span class="dates-range">Du samedi 1 au samedi 8</span>
    <span class="dates-month">septembre 2018</span>
  </header>

  <section class="info">
    <p class="resort">PLAGES CÉLESTE</p>
    <h1 class="country">BULGARIE</h1>
    <ul class="feature-list trip-basics">
      <li>VOYAGE "TOUT COMPRIS"</li>
      <li>VOL ALLER-RETOUR</li>
      <li>HÔTEL 4****</li>
    </ul>
    <p class="highlight formula">FORMULE ALL INCLUSIVE</p>
    <ul class="feature-list extras">
      <li>ENTRÉES EN BOITES</li>
      <li>COCKTAILS OFFERTS</li>
      <li>BEACH PARTY</li>
      <li class="highlight">... &amp; BIEN PLUS</li>
    </ul>
  </section>

  <div class="price">
    <span class="price-amount">PRIX : € 599,00</span>
    <span class="price-terms">par personne<br>en chambre double</span>
  </div>

  <div class="contact">
    <p class="contact-text">Plus d'infos sur :<br>www.golden-drift-trips.com<br>0472 818 604</p>
  </div>
</main>
</body>
</html>
```